Neues Flyer-Design gesucht
Zielgruppe
siehe Homepage www.lirok-bremen.de
Aufgabenstellung
Wir haben bereits einen Flyer und wünschen uns einen neuen, mit weniger Text und anderen Bildern. Wir sind auch offen für ein anderes Format.
In der Datei flyer_ueberarbeitung.docx haben wir andere Texte, sind jedoch nicht zufrieden damit und wünsche professionelle Hilfe :)

```html
<!DOCTYPE html>
<html lang="de">
<head>
<meta charset="utf-8">
<title>Lirok Soziale Dienste – Flyer Hilfen zur Erziehung</title>
<link href="https://fonts.googleapis.com/css2?family=Source+Sans+3:ital,wght@0,400;0,600;0,700;1,400;1,600&display=swap" rel="stylesheet">
<style>
:root{
  --green:#9cbb1a;
  --green-dark:#86a312;
  --green-soft:#c7d383;
  --green-pale:#e6ecc8;
  --ink:#444444;
  --ink-dark:#3b3b3b;
  --paper:#f4f4f4;
  --paper-shade:#e2e2e2;
  --stage:#e9e9e9;
  --white:#ffffff;
}
*{box-sizing:border-box;margin:0;padding:0}
html,body{width:840px;height:1200px;overflow:hidden}
body{background:var(--stage);font-family:"Source Sans 3",Arial,sans-serif;color:var(--ink);position:relative}
.spread{position:absolute;left:0;width:840px;height:594px;background:linear-gradient(90deg,var(--paper) 0%,var(--white) 30%,var(--paper-shade) 33.3%,var(--white) 36%,var(--white) 63%,var(--paper-shade) 66.6%,var(--white) 69%,var(--paper) 100%);overflow:hidden}
.spread--outside{top:4px}
.spread--inside{top:602px}
.spread svg.shapes{position:absolute;inset:0}
.abs{position:absolute}
h2{color:var(--green);font-weight:700;font-size:14px;line-height:1.1;margin-bottom:5px}
p,li{font-size:8.6px;line-height:1.32}
p+p{margin-top:6px}

/* outside */
.bubble{left:38px;top:148px;width:210px;height:158px;background:var(--green-soft);border-radius:16px;padding:14px 14px;color:var(--ink-dark)}
.bubble h2{color:var(--ink-dark);font-size:14px}
.bubble ul{list-style:none;margin:2px 0}
.bubble-tail{left:150px;top:300px}
.contact{left:305px;top:150px;width:240px}
.contact .person{font-size:9px;margin:10px 0 14px;line-height:1.3}
.contact-row{display:flex;align-items:flex-start;gap:8px;margin-bottom:9px;font-size:9px;line-height:1.3}
.contact-row svg{flex:none}
.badge{left:750px;top:16px;width:76px;height:76px;border-radius:50%;background:var(--ink-dark);border:3px solid var(--green);color:var(--white);font-size:8px;line-height:1.35;display:flex;align-items:center;justify-content:center;text-align:center}
.brand{left:600px;top:118px;display:flex;align-items:center;gap:10px;color:var(--green)}
.brand-dot{width:22px;height:22px;border-radius:50%;background:var(--green)}
.brand-name{font-size:26px;font-weight:600;line-height:1}
.brand-sub{font-size:13px;font-weight:600;line-height:1}
.cover-title{left:590px;top:170px;width:240px;text-align:center;font-size:19px;font-weight:700;color:var(--green)}
.cover-band{left:560px;top:470px;width:280px;text-align:center;color:var(--white);font-weight:700;font-size:13.5px;line-height:1.25}
.cover-url{left:560px;top:555px;width:280px;text-align:center;color:var(--white);font-size:12px}

/* inside */
.questions{left:40px;top:120px;width:230px;list-style:none}
.questions li{font-size:11px;font-weight:600;font-style:italic;color:var(--ink-dark);line-height:1.3;margin-bottom:12px;padding-left:14px;position:relative}
.questions li::before{content:"➔";position:absolute;left:0;top:0;color:var(--green);font-style:normal;font-size:10px}
.circle-note{left:20px;top:320px;width:190px;height:190px;border-radius:50%;background:var(--ink-dark);border:3px solid var(--green-soft);color:var(--white);display:flex;flex-direction:column;justify-content:center;align-items:center;text-align:center;padding:0 26px}
.circle-note p{font-size:10px;line-height:1.4}
.circle-note .strong{font-weight:600;margin-top:10px;font-size:10.5px}
.column{width:248px}
.col-mid{left:296px;top:82px}
.col-right{left:576px;top:28px}
.column h2{font-size:13px;margin-top:12px}
.column h2:first-child{margin-top:0}
.offer{margin-top:5px}
.offer strong{display:block;font-size:8.8px;color:var(--ink-dark)}
.offer strong::before{content:"➔ ";color:var(--green)}
.quote{font-style:italic;font-weight:600;margin-top:10px}
.inside-url{left:560px;top:570px;width:270px;text-align:right;color:var(--white);font-size:12px}
</style>
</head>
<body>

<!-- Outside of the trifold -->
<section class="spread spread--outside">
  <svg class="shapes" width="840" height="594" viewBox="0 0 840 594">
    <defs>
      <linearGradient id="skin" x1="0" x2="1" y1="0" y2="0">
        <stop offset="0" stop-color="#7fb2d6"/><stop offset=".35" stop-color="#c99a72"/><stop offset="1" stop-color="#e2c3a4"/>
      </linearGradient>
      <linearGradient id="room" x1="0" x2="1">
        <stop offset="0" stop-color="#8d8fa6"/><stop offset=".5" stop-color="#d9c4ac"/><stop offset="1" stop-color="#b79a7d"/>
      </linearGradient>
      <linearGradient id="family" x1="0" x2="0" y1="0" y2="1">
        <stop offset="0" stop-color="#f3efe6"/><stop offset=".5" stop-color="#e0c3a6"/><stop offset="1" stop-color="#c7a78c"/>
      </linearGradient>
    </defs>
    <path d="M0 0H560V38C420 60 230 112 0 100Z" fill="url(#skin)" role="img" aria-label="Foto: Kinderhände und Erwachsenenhand halten sich"/>
    <path d="M0 104C230 116 420 64 560 44" fill="none" stroke="#c7d383" stroke-width="4"/>
    <path d="M0 415C160 440 360 470 560 462V594H0Z" fill="url(#room)" role="img" aria-label="Foto: Familie mit Baby und Kleinkind im Wohnzimmer, Kinder liegen lachend auf dem Boden"/>
    <path d="M0 410C160 435 360 465 560 457" fill="none" stroke="#c7d383" stroke-width="4"/>
    <path d="M580 206H840V420C760 440 660 452 580 456Z" fill="url(#family)" role="img" aria-label="Foto: lachende Familie mit zwei Kindern"/>
    <path d="M560 460C660 452 760 430 840 400V594H560Z" fill="#9cbb1a"/>
    <path d="M560 452C660 444 760 422 840 392" fill="none" stroke="#c7d383" stroke-width="5"/>
  </svg>

  <div class="abs bubble">
    <h2>Sprachliche Vielfalt</h2>
    <p>Unsere Mitarbeiter/innen verfügen über unterschiedliche kulturelle und sprachliche Hintergründe.</p>
    <p>Wir haben daher die Möglichkeit Ihnen auch auf:</p>
    <ul><li>• Arabisch</li><li>• Kurdisch</li><li>• Türkisch</li><li>• Englisch</li></ul>
    <p>eine Betreuung anzubieten.</p>
  </div>
  <svg class="abs bubble-tail" width="40" height="34" viewBox="0 0 40 34"><path d="M0 0H40L14 34Z" fill="#c7d383"/></svg>

  <div class="abs contact">
    <h2>Kontakt</h2>
    <p class="person">Ansprechpartnerin<br>Frau Marta Kessler</p>
    <div class="contact-row">
      <svg width="14" height="14" viewBox="0 0 14 14"><circle cx="7" cy="7" r="7" fill="#9cbb1a"/><path d="M7 3a2.4 2.4 0 0 0-2.4 2.4C4.6 7.3 7 10.5 7 10.5s2.4-3.2 2.4-5.1A2.4 2.4 0 0 0 7 3z" fill="#fff"/></svg>
      <span>Lirok – Soziale Dienste<br>Lindenweg 14<br>28195 Bremen-Mitte</span>
    </div>
    <div class="contact-row">
      <svg width="14" height="14" viewBox="0 0 14 14"><circle cx="7" cy="7" r="7" fill="#9cbb1a"/><circle cx="7" cy="7" r="3.6" fill="none" stroke="#fff" stroke-width="1"/><path d="M3.4 7h7.2M7 3.4v7.2" stroke="#fff" stroke-width=".8"/></svg>
      <span>www.lirok-bremen.de</span>
    </div>
    <div class="contact-row">
      <svg width="14" height="14" viewBox="0 0 14 14"><circle cx="7" cy="7" r="7" fill="#9cbb1a"/><rect x="3.5" y="4.5" width="7" height="5" fill="none" stroke="#fff" stroke-width="1"/><path d="M3.5 4.5L7 7.5l3.5-3" fill="none" stroke="#fff" stroke-width="1"/></svg>
      <span>info@lirok-bremen.de</span>
    </div>
    <div class="contact-row">
      <svg width="14" height="14" viewBox="0 0 14 14"><circle cx="7" cy="7" r="7" fill="#9cbb1a"/><rect x="5" y="3.2" width="4" height="7.6" rx="1" fill="#fff"/></svg>
      <span>Tel: 0421/498 310 27</span>
    </div>
  </div>

  <div class="abs badge">Betreuung<br>Begleitung<br>Unterstützung</div>
  <div class="abs brand">
    <span class="brand-dot"></span>
    <span><span class="brand-name">Lirok</span><br><span class="brand-sub">Soziale Dienste</span></span>
  </div>
  <div class="abs cover-title">Hilfen zur Erziehung</div>
  <div class="abs cover-band">Sozialpädagogische Familienhilfe<br>Erziehungsbeistand</div>
  <div class="abs cover-url">www.lirok-bremen.de</div>
</section>

<!-- Inside of the trifold -->
<section class="spread spread--inside">
  <svg class="shapes" width="840" height="594" viewBox="0 0 840 594">
    <defs>
      <linearGradient id="kids" x1="0" x2="1">
        <stop offset="0" stop-color="#e88ab8"/><stop offset=".4" stop-color="#c98e6a"/><stop offset=".8" stop-color="#e7c9a9"/><stop offset="1" stop-color="#6fb4da"/>
      </linearGradient>
      <linearGradient id="sunset" x1="0" x2="0" y1="0" y2="1">
        <stop offset="0" stop-color="#f6f1e6"/><stop offset=".45" stop-color="#e8cf9a"/><stop offset=".8" stop-color="#c89a55"/><stop offset="1" stop-color="#a8782f"/>
      </linearGradient>
    </defs>
    <path d="M0 0H600V8C430 20 250 70 0 86Z" fill="url(#kids)" role="img" aria-label="Foto: Kinder liegen lachend nebeneinander"/>
    <path d="M0 90C250 74 430 24 640 4" fill="none" stroke="#c7d383" stroke-width="4"/>
    <path d="M0 360C250 420 520 440 840 420V594H0Z" fill="url(#sunset)" role="img" aria-label="Foto: Familie läuft mit ausgebreiteten Armen über ein Feld im Sonnenuntergang"/>
    <path d="M0 585C300 580 600 570 840 540V594H0Z" fill="#9cbb1a"/>
    <path d="M0 580C300 575 600 565 840 535" fill="none" stroke="#c7d383" stroke-width="4"/>
  </svg>

  <ul class="abs questions">
    <li>Wünschen Sie eine pädagogische Unterstützung für Ihre Familie?</li>
    <li>Sind Sie oder Ihre Familie durch Konflikte belastet, die Sie am liebsten aus der Welt schaffen würden?</li>
    <li>Wünschen Sie sich eine Unterstützung in der Kooperation mit Schulen und Kitas oder auch in Behördenangelegenheiten?</li>
  </ul>

  <div class="abs circle-note">
    <p>Im Laufe eines Lebens können Situationen und Umstände entstehen, welche allein nur schwierig oder gar nicht bewältigt werden können.</p>
    <p class="strong">Gerne stehen wir Ihnen dabei zur Seite.</p>
  </div>

  <div class="abs column col-mid">
    <h2>Wer wir sind</h2>
    <p>Wir sind ein Team von pädagogischen Fachkräften, welches vorrangig Erziehungsberatung leistet.</p>
    <p>Lirok-Soziale Dienste ist ein freier Träger der Kinder- und Jugendhilfe und arbeitet nach dem Kinder- und Jugendhilferecht des 8. Sozialgesetzbuches.</p>
    <p>Das heißt, wir bieten eine pädagogische Unterstützung im Rahmen einer sogenannten „Hilfe zur Erziehung“ an.</p>
    <h2>Was wir anbieten</h2>
    <div class="offer"><strong>Sozialpädagogische Familienhilfe</strong><p>Im Rahmen einer sozialpädagogischen Familienhilfe erfahren Familien direkt vor Ort eine pädagogische Unterstützung, vor allem in Form einer Erziehungsberatung.</p></div>
    <div class="offer"><strong>Erziehungsbeistandschaft, auch für junge Volljährige</strong><p>Mit einer Erziehungsbeistandschaft wird einem Kind oder Jugendlichen exklusiv eine pädagogische Fachkraft an die Seite gestellt. Ziel ist die Unterstützung des Kindes oder Jugendlichen in einer bestimmten Zeit.</p></div>
    <div class="offer"><strong>Begleitete Umgänge</strong><p>Nach einer Trennung der Eltern und/oder Gewaltvorwürfen kann es sinnvoll sein, dass die Kontakte zwischen einem Elternteil und Kind pädagogisch begleitet werden.</p></div>
  </div>

  <div class="abs column col-right">
    <h2>Wie Sie Unterstützung erhalten</h2>
    <p>Sollten Sie eine pädagogische Unterstützung wünschen, ist der Allgemeine Soziale Dienst (ASD) des Jugendamtes Ihre erste Anlaufstelle. Mit Hilfe des Behördenfinders wissen Sie, welcher ASD für Sie zuständig ist:<br><i>www.stadtportal-bremen.de/behoerden</i></p>
    <p>Im Gespräch mit dem ASD wird geprüft, ob ein pädagogischer Bedarf vorliegt. Falls dies zutrifft, wird mit Ihnen besprochen, welche Unterstützung für Sie am besten geeignet sein könnte.</p>
    <h2>Was uns wichtig ist</h2>
    <p>Wir sehen es als unsere Aufgabe an, mit den KlientInnen partizipativ die eigenen Stärken zu aktivieren und sozialraumorientiert zu arbeiten, indem wir Netzwerke und Sozialräume mit den KlientInnen erschließen, die sie im Alltag unterstützen. Die besondere Bedeutung hinsichtlich Sensibilität, Wertschätzung, Offenheit, Toleranz und Transparenz im Umgang mit anderen Menschen kann nicht hoch genug eingeschätzt werden.</p>
    <p class="quote">Helene Marwitz hat dies folgendermaßen formuliert: Wer anderen Mut schenkt, findet ihn auch in sich selbst. Vertrauen lässt jede Stärke wachsen.</p>
  </div>

  <div class="abs inside-url">www.lirok-bremen.de</div>
</section>

</body>
</html>
```